Oil and Gas Exploration and Production company needs a business card design

We need a business card design using our logo and colors in the logo. We want a mainstream design.

```html
<!DOCTYPE html>
<html lang="en">
<head>
<meta charset="UTF-8">
<title>Norvik Oil &amp; Gas – Business Card</title>
<link href="https://fonts.googleapis.com/css2?family=Roboto:wght@400;500;700&family=Roboto+Condensed:wght@700&display=swap" rel="stylesheet">
<style>
  :root {
    --backdrop: #2b2b2b;
    --card: #1e1e1e;
    --white: #f4f4f4;
    --gold: #d9a521;
    --rule: #8a8a8a;
  }
  * { margin: 0; padding: 0; box-sizing: border-box; }
  html, body {
    width: 1200px; height: 900px; overflow: hidden;
    background: var(--backdrop);
    font-family: "Roboto", Arial, sans-serif;
    color: var(--white);
  }
  .stage {
    width: 1200px; height: 900px;
    display: flex; flex-direction: column; align-items: center; justify-content: center;
    gap: 46px;
  }
  .card {
    position: relative;
    width: 680px; height: 388px;
    background: var(--card);
    box-shadow: 0 10px 30px rgba(0,0,0,.45);
  }
  /* Front */
  .card-front {
    display: flex; flex-direction: column; align-items: center; justify-content: center;
  }
  .brand {
    display: flex; align-items: center; gap: 18px;
  }
  .brand-dot {
    width: 46px; height: 46px; border-radius: 50%;
    background: var(--gold);
  }
  .brand-name {
    font-weight: 700; font-size: 50px; line-height: 1;
    color: var(--white); letter-spacing: 1px;
  }
  .front-web {
    margin-top: 46px;
    font-size: 15px; letter-spacing: 6px; color: var(--white);
  }
  /* Back */
  .identity {
    position: absolute; right: 362px; top: 136px; text-align: right;
  }
  .person-name {
    font-family: "Roboto Condensed", Arial, sans-serif;
    font-weight: 700; font-size: 34px; line-height: 1; letter-spacing: .5px;
  }
  .person-title {
    margin-top: 6px;
    font-family: "Roboto Condensed", Arial, sans-serif;
    font-weight: 700; font-size: 18px; color: var(--gold);
  }
  .divider {
    position: absolute; left: 336px; top: 112px;
    width: 1.5px; height: 130px; background: var(--rule);
  }
  .contacts {
    position: absolute; left: 362px; top: 116px;
    list-style: none;
  }
  .contacts li {
    display: flex; align-items: center; gap: 12px;
    font-size: 17px; line-height: 24px;
  }
  .contacts svg { width: 15px; height: 15px; fill: var(--white); flex: none; }
  .address {
    position: absolute; left: 150px; bottom: 44px;
    display: flex; align-items: center; gap: 8px;
    font-size: 18px;
  }
  .address svg { width: 14px; height: 18px; fill: var(--white); }
</style>
</head>
<body>
<main class="stage">
  <section class="card card-front">
    <div class="brand">
      <span class="brand-dot"></span>
      <span class="brand-name">Norvik Oil &amp; Gas</span>
    </div>
    <p class="front-web">www.norvikoil.com</p>
  </section>

  <section class="card card-back">
    <div class="identity">
      <h1 class="person-name">DANIEL REYES</h1>
      <p class="person-title">CEO/FOUNDER</p>
    </div>
    <span class="divider"></span>
    <ul class="contacts">
      <li>
        <svg viewBox="0 0 16 16"><path d="M3.6 1.2l2.3 2.6-1.3 1.9c.9 2 2.4 3.6 4.5 4.6l1.9-1.3 2.6 2.3-1.2 2.6C7.4 13.7 2.3 8.6 1 3.6z"/></svg>
        612 555 0148
      </li>
      <li>
        <svg viewBox="0 0 16 16"><path d="M4 0h8a1 1 0 0 1 1 1v14a1 1 0 0 1-1 1H4a1 1 0 0 1-1-1V1a1 1 0 0 1 1-1zm1 2v10h6V2zm3 11a1 1 0 1 0 0 2 1 1 0 0 0 0-2z"/></svg>
        612 555 0193
      </li>
      <li>
        <svg viewBox="0 0 16 16"><path d="M4 1h8v4H4zM1 6h14v6h-3v3H4v-3H1zm4 4v4h6v-4z"/></svg>
        612 555 0176
      </li>
      <li>
        <svg viewBox="0 0 16 16"><path d="M1 3h14v10H1zm1.5 1.2v.4L8 8.6l5.5-4v-.4z"/></svg>
        info@norvikoil.com
      </li>
      <li>
        <svg viewBox="0 0 16 16"><path d="M8 1a7 7 0 1 0 0 14A7 7 0 0 0 8 1zm0 1.5c.8 1 1.4 2.6 1.6 4.5H6.4C6.6 5.1 7.2 3.5 8 2.5zM2.6 9h2.3c.1 1.6.5 3 1.1 4.1A5.5 5.5 0 0 1 2.6 9zm0-2A5.5 5.5 0 0 1 6 2.9C5.4 4 5 5.4 4.9 7zm8.5 2h2.3A5.5 5.5 0 0 1 10 13.1c.6-1.1 1-2.5 1.1-4.1zm0-2c-.1-1.6-.5-3-1.1-4.1A5.5 5.5 0 0 1 13.4 7zM6.4 9h3.2c-.2 1.9-.8 3.5-1.6 4.5-.8-1-1.4-2.6-1.6-4.5z"/></svg>
        www.norvikoil.com
      </li>
    </ul>
    <p class="address">
      <svg viewBox="0 0 14 18"><path d="M7 0a7 7 0 0 0-7 7c0 5 7 11 7 11s7-6 7-11a7 7 0 0 0-7-7zm0 4a3 3 0 1 1 0 6 3 3 0 0 1 0-6z"/></svg>
      4120 Birchwood Road, Anchorage, Alaska 99503
    </p>
  </section>
</main>
</body>
</html>
```